Harborline Insulation Inc facebook rebranding

We had our facebook design done 3 years ago and we need to get it more updated and attractive. I have attached what we already use and here below is a link to our page. i have 2 locations so when we pick a design we will need files to have each locations logo and phone number
location 1- Harborline Insulation Inc. 469-555-0172
Location 2- Harborline Insulation of west texas inc. 806-555-0148
here is link
Target Market(s)
contractors and homeowners
Industry/Entity Type
Insulation
Font styles to use
Serif
Colors
0054AA
0677BA
7BADD7
CADEEF
E8F1F8

```html
<!DOCTYPE html>
<html lang="en">
<head>
<meta charset="utf-8">
<title>Harborline Insulation – Facebook Cover, Both Locations</title>
<link rel="stylesheet" href="https://fonts.googleapis.com/css2?family=Cinzel:wght@500;600;700&family=Oswald:wght@300;400;500&display=swap">
<style>
  :root {
    --deep-blue: #0054AA;
    --ocean-blue: #0677BA;
    --sky-blue: #7BADD7;
    --mist-blue: #CADEEF;
    --ice-blue: #E8F1F8;
    --navy: #0a1f4a;
    --ring-blue: #1156a8;
    --white: #ffffff;
  }
  html, body {
    margin: 0;
    padding: 0;
    width: 1200px;
    height: 676px;
    overflow: hidden;
    background: var(--ice-blue);
  }
  .cover {
    display: block;
    width: 1200px;
    height: 676px;
  }
  .services-line {
    font-family: "Oswald", sans-serif;
    font-weight: 400;
    font-size: 25px;
    fill: var(--mist-blue);
  }
  .tagline {
    font-family: "Oswald", sans-serif;
    font-weight: 400;
    font-size: 21px;
    fill: var(--ice-blue);
  }
  .contact-heading {
    font-family: "Cinzel", serif;
    font-weight: 600;
    font-size: 50px;
    fill: var(--white);
  }
  .location-name {
    font-family: "Oswald", sans-serif;
    font-weight: 400;
    font-size: 17px;
    letter-spacing: 3px;
    fill: var(--mist-blue);
  }
  .location-phone {
    font-family: "Cinzel", serif;
    font-weight: 600;
    font-size: 44px;
    fill: var(--white);
  }
  .website {
    font-family: "Cinzel", serif;
    font-weight: 500;
    font-size: 20px;
    letter-spacing: 1px;
    fill: var(--white);
  }
</style>
</head>
<body>
<svg class="cover" viewBox="0 0 1200 676" xmlns="http://www.w3.org/2000/svg">
  <defs>
    <linearGradient id="bgGradient" x1="0" y1="0" x2="1" y2="0">
      <stop offset="0" stop-color="#E8F1F8"/>
      <stop offset="0.3" stop-color="#3d8fcc"/>
      <stop offset="0.5" stop-color="#0677BA"/>
      <stop offset="0.75" stop-color="#0c4c99"/>
      <stop offset="1" stop-color="#0a1f4a"/>
    </linearGradient>
    <linearGradient id="sprayPhotoTone" x1="0" y1="0" x2="1" y2="1">
      <stop offset="0" stop-color="#b08a5c"/>
      <stop offset="0.55" stop-color="#6b5a4a"/>
      <stop offset="1" stop-color="#2e3345"/>
    </linearGradient>
    <linearGradient id="roomPhotoTone" x1="0" y1="0" x2="0" y2="1">
      <stop offset="0" stop-color="#b8875a"/>
      <stop offset="0.5" stop-color="#d9c6a8"/>
      <stop offset="1" stop-color="#8a7d70"/>
    </linearGradient>
  </defs>

  <rect class="background" width="1200" height="676" fill="url(#bgGradient)"/>

  <g class="decor-circles">
    <circle cx="439" cy="23" r="62" fill="var(--ring-blue)"/>
    <circle cx="439" cy="23" r="33" fill="#4a9ad4"/>
    <circle cx="983" cy="7" r="16" fill="#1a5eb0"/>
    <circle cx="983" cy="7" r="6" fill="#0a3a7a"/>
    <circle cx="1000" cy="477" r="29" fill="#1156a8"/>
    <circle cx="1054" cy="673" r="104" fill="#0f4fa0"/>
    <circle cx="1054" cy="673" r="48" fill="#0a2e6a"/>
    <circle cx="1191" cy="604" r="35" fill="#1156a8"/>
    <circle cx="1191" cy="604" r="16" fill="#0a2550"/>
  </g>

  <g class="photo-frame primary">
    <circle cx="198" cy="263" r="282" fill="var(--ring-blue)"/>
    <circle cx="194" cy="252" r="236" fill="url(#sprayPhotoTone)" role="img" aria-label="Photo of an installer in a protective suit applying spray foam insulation to a wall"/>
  </g>

  <g class="photo-frame secondary">
    <circle cx="406" cy="512" r="183" fill="var(--ring-blue)"/>
    <circle cx="406" cy="512" r="155" fill="url(#roomPhotoTone)" role="img" aria-label="Photo of a framed room with walls filled with spray foam insulation"/>
  </g>

  <text class="services-line" x="790" y="102" text-anchor="middle" textLength="660" lengthAdjust="spacing">SPRAY FOAM  -  FIBERGLASS  -  INSULATION  -  ROOFING</text>
  <text class="tagline" x="790" y="164" text-anchor="middle" textLength="500" lengthAdjust="spacing">DFW PREMIER INSULATION COMPANY</text>

  <text class="contact-heading" x="850" y="238" text-anchor="middle" textLength="400" lengthAdjust="spacing">CONTACT US:</text>

  <g class="location location-dfw">
    <text class="location-name" x="850" y="284" text-anchor="middle">HARBORLINE INSULATION INC.</text>
    <text class="location-phone" x="850" y="334" text-anchor="middle" textLength="370" lengthAdjust="spacing">469-555-0172</text>
  </g>

  <line class="location-divider" x1="790" y1="362" x2="910" y2="362" stroke="var(--sky-blue)" stroke-width="2"/>

  <g class="location location-west-texas">
    <text class="location-name" x="850" y="396" text-anchor="middle">HARBORLINE INSULATION OF WEST TEXAS INC.</text>
    <text class="location-phone" x="850" y="446" text-anchor="middle" textLength="370" lengthAdjust="spacing">806-555-0148</text>
  </g>

  <rect class="website-pill" x="620" y="484" width="460" height="64" rx="32" fill="var(--sky-blue)"/>
  <text class="website" x="850" y="523" text-anchor="middle">HARBORLINEINSULATION.COM</text>
</svg>
</body>
</html>
```